ZOVA Framework. the way you communicate in every situation and in all environments.

I would like you to create a diagram depicting a very specific process of communication. it must follow the look of the diagram that i have attached. this is going to be used in a book called BEDROCK. it is going to explain the fact that we communicate all the same way using this process as we communicate. it starts with the fact that everyone takes everything that is said personally and then moves on to filters, which is your own agenda or experience kicking in. then you move to your why it matters, which is your motivation and ends with the choice of words you use when you communicate. if you are going to be successful then you must separate the person from the issue.

Target Market(s)

market is executive business people around the world

Industry/Entity Type

Consulting

Font styles to use
Sans Serif

Colors

Designer to choose only greyscale colors for use in the design.

Requirements
Must have
• I would like it to have a diving/ocean/snorkel feel to it. The analogy we are using is to make a deep dive when you are communicating. it must have every part of the diagram you see, it starts at the top with the zova framework (and the words) it then connects to the filters which connects to the why it matters with connects to the words and then end with the separating the person from the issue.
Nice to have
• we are writing a black and white book NO color. therefore the words should be clear and easy to read. Each section should be able to stand on its own so we can write about it separately.
Should not have
• the diagram DOES NOT have to look like the one i gave you. it must explain the fact that it starts with ZOVA and ends with Separate and must pass through the three areas to get to the SEPARATE.

```html
<!DOCTYPE html>
<html lang="en">
<head>
<meta charset="utf-8">
<title>ZOVA Framework – Communication Cycle</title>
<link rel="stylesheet" href="https://fonts.googleapis.com/css2?family=Montserrat:wght@700&family=Poppins:wght@400&display=swap">
<style>
  :root {
    --page: #ffffff;
    --band: #7b7b7b;
    --band-text: #ffffff;
    --segment-light: #ffffff;
    --segment-edge: #e4e4e4;
    --segment-outline: #5e5e5e;
    --body-text: #1f1f1f;
  }
  html, body {
    margin: 0;
    padding: 0;
    width: 1200px;
    height: 1200px;
    overflow: hidden;
    background: var(--page);
  }
  .canvas {
    width: 1200px;
    height: 1200px;
    background: var(--page);
  }
  .cycle {
    display: block;
    width: 1200px;
    height: 1200px;
  }
  .segment {
    fill: url(#segmentShade);
    stroke: var(--segment-outline);
    stroke-width: 1.6;
  }
  .band {
    fill: var(--band);
  }
  .band-label {
    font-family: "Montserrat", sans-serif;
    font-weight: 700;
    font-size: 47px;
    letter-spacing: 1px;
    fill: var(--band-text);
  }
  .segment-copy {
    font-family: "Poppins", sans-serif;
    font-weight: 400;
    font-size: 26px;
    fill: var(--body-text);
    text-anchor: middle;
  }
</style>
</head>
<body>
<main class="canvas">
  <svg class="cycle" viewBox="0 0 1330 1330" xmlns="http://www.w3.org/2000/svg" role="img" aria-label="ZOVA Framework communication cycle: ZOVA Framework, Your Filters, Why It Matters, Your Words, What To Do">
    <defs>
      <radialGradient id="segmentShade" cx="0" cy="0" r="400" gradientUnits="userSpaceOnUse">
        <stop offset="0.35" stop-color="var(--segment-light)"/>
        <stop offset="1" stop-color="var(--segment-edge)"/>
      </radialGradient>
      <path id="segmentShape" d="M 117.8 -75.6 L 324.3 -225.4 A 395 395 0 0 1 324.3 225.4 L 117.8 75.6 A 140 140 0 0 0 117.8 -75.6 Z"/>
      <path id="bandShape" d="M 335.9 -235.2 L 413.7 -289.7 A 505 505 0 0 1 413.7 289.7 L 335.9 235.2 A 410 410 0 0 0 335.9 -235.2 Z"/>
      <path id="arcOver" d="M 359.6 -251.8 A 439 439 0 0 1 359.6 251.8"/>
      <path id="arcUnder" d="M 389.1 272.4 A 475 475 0 0 0 389.1 -272.4"/>
    </defs>

    <g class="ring" transform="translate(666 660)">
      <!-- ZOVA Framework -->
      <g class="stage stage-framework" transform="rotate(-128)">
        <use href="#segmentShape" class="segment"/>
        <use href="#bandShape" class="band"/>
        <text class="band-label"><textPath href="#arcOver" startOffset="50%" text-anchor="middle">ZOVA FRAMEWORK</textPath></text>
      </g>
      <!-- What to do -->
      <g class="stage stage-action" transform="rotate(-56)">
        <use href="#segmentShape" class="segment"/>
        <use href="#bandShape" class="band"/>
        <text class="band-label"><textPath href="#arcOver" startOffset="50%" text-anchor="middle">WHAT TO DO</textPath></text>
      </g>
      <!-- Your words -->
      <g class="stage stage-words" transform="rotate(16)">
        <use href="#segmentShape" class="segment"/>
        <use href="#bandShape" class="band"/>
        <text class="band-label"><textPath href="#arcUnder" startOffset="50%" text-anchor="middle">YOUR WORDS</textPath></text>
      </g>
      <!-- Why it matters -->
      <g class="stage stage-motivation" transform="rotate(88)">
        <use href="#segmentShape" class="segment"/>
        <use href="#bandShape" class="band"/>
        <text class="band-label"><textPath href="#arcUnder" startOffset="50%" text-anchor="middle">WHY IT MATTERS</textPath></text>
      </g>
      <!-- Your filters -->
      <g class="stage stage-filters" transform="rotate(160)">
        <use href="#segmentShape" class="segment"/>
        <use href="#bandShape" class="band"/>
        <text class="band-label"><textPath href="#arcUnder" startOffset="50%" text-anchor="middle">YOUR FILTERS</textPath></text>
      </g>
    </g>

    <text class="segment-copy copy-framework">
      <tspan x="481" y="439">When words are</tspan>
      <tspan x="481" y="476">taken personally,</tspan>
      <tspan x="481" y="512">what happens?</tspan>
    </text>

    <text class="segment-copy copy-action">
      <tspan x="848" y="442">Separate the</tspan>
      <tspan x="848" y="479">Person from</tspan>
      <tspan x="848" y="517">the Issue</tspan>
    </text>

    <text class="segment-copy copy-words">
      <tspan x="921" y="702">This is your</tspan>
      <tspan x="921" y="739">immediate</tspan>
      <tspan x="921" y="776">response, verbal</tspan>
      <tspan x="921" y="812">or perhaps</tspan>
      <tspan x="921" y="849">non-verbal</tspan>
    </text>

    <text class="segment-copy copy-motivation">
      <tspan x="660" y="899">This is your</tspan>
      <tspan x="660" y="937">compass. It is what</tspan>
      <tspan x="660" y="975">motivates you,</tspan>
      <tspan x="660" y="1013">what drives you.</tspan>
    </text>

    <text class="segment-copy copy-filters">
      <tspan x="410" y="721">An accumulation</tspan>
      <tspan x="410" y="758">of your experience,</tspan>
      <tspan x="410" y="794">knowledge and</tspan>
      <tspan x="410" y="829">values</tspan>
    </text>
  </svg>
</main>
</body>
</html>
```